We need motivational posters designed to be used in classrooms at a truck driving school. The purpose of the posters is to motivate the students.

I want the the quotes to be the main focal point of emphasis and our logo on the bottom of the poster for branding purposes.

I would like the images to be related to the trucking industry

Below are the quotes for the posters

Poster 1
"Start where you are. Use what you have. Do what you can."
-Dorian Vell-

Poster 2
"The secret of getting ahead is getting started"
-Lewis Crane-

Poster 3
"Most effective way to do it, is to do it."
-Odessa Brindle-

Poster 4
"Set your goals big, and don't stop till you get there."
-Cy Morrow-

Poster 5
"If you are not willing to learn, no one can help you. If you are determined to learn, no one can stop you."
-Unknown-

Poster 6
"The will to succeed is important, but what's more important is the will to prepare."
-Teddy Sloane-

THESE POSTERS SHOULD BE DESIGNED AS 18X24
LANDSCAPE AND PORTRAIT ORIENTATION

```html
<!DOCTYPE html>
<html lang="en">
<head>
<meta charset="utf-8">
<title>Motivational Poster – Start Where You Are</title>
<link rel="stylesheet" href="https://fonts.googleapis.com/css2?family=Bebas+Neue&display=swap">
<style>
  :root {
    --backdrop: #3b3b3b;
    --paper: #ffffff;
    --lime: #c4cd32;
    --sky-blue: #80bdc7;
    --orange: #d4601f;
    --attribution-grey: #9b9b9b;
    --brand-ink: #2a2f36;
    --band-sky-top: #b9cde0;
    --band-sky-mid: #dfe8ee;
    --band-ground: #7f9a5a;
  }
  html, body {
    margin: 0;
    padding: 0;
    width: 1200px;
    height: 800px;
    overflow: hidden;
    background: var(--backdrop);
  }
  .poster-canvas {
    display: block;
    width: 1200px;
    height: 800px;
  }
  .poster-sheet { fill: var(--paper); }
  .quote-text {
    font-family: "Bebas Neue", "Oswald", sans-serif;
    font-weight: 400;
  }
  .quote-line-start { fill: var(--lime); }
  .quote-line-use { fill: var(--sky-blue); }
  .quote-line-do { fill: var(--orange); }
  .quote-mark-open { fill: var(--lime); }
  .quote-mark-close { fill: var(--orange); }
  .quote-author {
    font-family: "Bebas Neue", "Oswald", sans-serif;
    fill: var(--attribution-grey);
  }
  .brand-band-sky-top { stop-color: var(--band-sky-top); }
  .brand-band-sky-mid { stop-color: var(--band-sky-mid); }
  .brand-band-ground { stop-color: var(--band-ground); }
  .brand-mark-dot { fill: var(--brand-ink); }
  .brand-name {
    font-family: "Bebas Neue", "Oswald", sans-serif;
    fill: var(--brand-ink);
  }
</style>
</head>
<body>
<svg class="poster-canvas" viewBox="0 0 1200 800" xmlns="http://www.w3.org/2000/svg">
  <defs>
    <linearGradient id="brand-band-fill" x1="0" y1="0" x2="0" y2="1">
      <stop class="brand-band-sky-top" offset="0"/>
      <stop class="brand-band-sky-mid" offset="0.7"/>
      <stop class="brand-band-ground" offset="0.86"/>
      <stop class="brand-band-ground" offset="1"/>
    </linearGradient>
  </defs>

  <g class="poster">
    <rect class="poster-sheet" x="205" y="127" width="780" height="550"/>

    <g class="quote-mark-open" aria-hidden="true">
      <polygon points="238,160 265,160 259,215 244,215"/>
      <polygon points="280,160 308,160 302,215 286,215"/>
    </g>

    <text class="quote-text quote-line-start" x="238" y="305" font-size="110"
          textLength="730" lengthAdjust="spacingAndGlyphs">START WHERE YOU ARE.</text>
    <text class="quote-text quote-line-use" x="238" y="365" font-size="67"
          textLength="440" lengthAdjust="spacingAndGlyphs">USE WHAT YOU HAVE.</text>
    <text class="quote-text quote-line-do" x="234" y="470" font-size="131"
          textLength="728" lengthAdjust="spacingAndGlyphs">DO WHAT YOU CAN.</text>

    <g class="quote-mark-close" aria-hidden="true">
      <polygon points="236,490 262,490 256,548 242,548"/>
      <polygon points="276,490 302,490 296,548 282,548"/>
    </g>

    <text class="quote-author" x="958" y="575" font-size="42" text-anchor="end">-DORIAN VELL-</text>

    <g class="brand-band">
      <rect x="205" y="585" width="780" height="92" fill="url(#brand-band-fill)"
            role="img" aria-label="Photo of a white semi truck with trailer driving on a flat highway under a blue cloudy sky"/>
      <circle class="brand-mark-dot" cx="256" cy="624" r="18"/>
      <text class="brand-name" x="282" y="632" font-size="22">SUMMIT HAUL DRIVING ACADEMY</text>
    </g>
  </g>
</svg>
</body>
</html>
```